Icon-Design für Makeup Artist Webseite
Super creative designs. Exactly what we were looking for!Highly recommended.
Zielgruppe
Sabine Ter Horst Makeup Artist. Zielgruppe 18-34. 'Normale' Personen die lernen wollen wie man Makeup richtig aufträgt.
Aufgabenstellung
Das Projekt besteht darin 5 Icons zu designen. Die Webseite ist noch in der Entwicklung ein Screenshot wie es auf dem Handy aussehen soll finden Sie im Anhang.
Es werden 5 creative Icons benötigt die die Kategorien wiederspiegeln.(Also keine "Langweiligen Icone", diese können ruhig ausgefallen sein, sollten jedoch zum style der Seite passen )
Kategorie 1 = Eye Makeup(Lidschatten) Tutorials. Hier sind Texte + Videos enthalten wie man das Augenmakeup richtig aufträgt + Ausgefallene Looks
Kategorie 2 = Skin Care. Texte+Bilder über Haut+Produkte zur richtigen Pflege seiner Haut.
Kategorie 3 = E-Book. Hier steht ein E-Book-Shop zur verfügung indem man sich E-Book kaufen kann.
Kategorie 4 = About. Hier sind alle Informationen über Sabine enthalten.
Download Button = Dieser sollte auf einem leicht grauen-weißen hintergrund ordentlich zum vorschein kommen.
Der Blaue Farb-Code der Webseite ist : 3b5998

```html
<!DOCTYPE html>
<html lang="en">
<head>
<meta charset="utf-8">
<title>Sabine Ter Horst – Mobile Home</title>
<link rel="stylesheet" href="https://fonts.googleapis.com/css2?family=Figtree:wght@400;600;700&display=swap">
<style>
  :root {
    --brand-blue: #3b5998;
    --brand-gold: #c9a44a;
    --lipstick-red: #b3102e;
    --page-bg: #f1f1f3;
    --screen-bg: #ffffff;
    --banner-tint: #fbeef0;
    --white: #ffffff;
  }
  * { box-sizing: border-box; margin: 0; padding: 0; }
  html, body {
    width: 1200px; height: 1200px; overflow: hidden;
    background: var(--page-bg);
    font-family: "Figtree", sans-serif;
  }
  .canvas {
    width: 1200px; height: 1200px;
    display: flex; align-items: center; justify-content: center;
  }
  .mobile-screen {
    width: 660px; height: 1129px;
    background: var(--screen-bg);
    display: flex; flex-direction: column;
    box-shadow: 0 4px 18px rgba(0,0,0,0.12);
  }

  /* Header */
  .site-header {
    height: 139px; background: var(--brand-blue);
    position: relative; display: flex; align-items: center; justify-content: center;
  }
  .menu-toggle {
    position: absolute; left: 43px; top: 50%; transform: translateY(-50%);
    width: 50px; height: 46px;
    display: flex; flex-direction: column; justify-content: space-between;
  }
  .menu-toggle span { display: block; height: 5px; border-radius: 3px; background: var(--white); }
  .brand-name {
    color: var(--brand-gold); font-weight: 700; font-size: 34px; letter-spacing: 0.5px;
  }

  /* Category icons */
  .category-nav {
    height: 172px; display: flex; justify-content: space-around; align-items: center;
    padding: 0 40px;
  }
  .category-icon { width: 90px; height: 90px; display: block; }

  /* Banner */
  .hero-banner {
    height: 347px; position: relative;
    background: linear-gradient(to bottom, var(--banner-tint) 0%, var(--white) 28%);
  }
  .hero-title {
    position: absolute; top: 36px; width: 100%; text-align: center;
    color: var(--lipstick-red); font-weight: 400; font-size: 50px; letter-spacing: 1px;
  }
  .hero-photo {
    position: absolute; left: 0; right: 0; bottom: 0; height: 235px;
    background: linear-gradient(to bottom, #d07a72 0%, #b5203d 35%, #8e1a4a 60%, #1e1a1c 85%, #141214 100%);
  }

  /* Guide promo */
  .guide-promo { height: 356px; position: relative; }
  .guide-heading {
    position: absolute; left: 52px; top: 60px;
    color: var(--brand-blue); font-weight: 400; font-size: 37px; line-height: 44px;
    text-transform: uppercase;
  }
  .download-button {
    position: absolute; left: 45px; top: 230px; width: 342px; height: 66px;
    background: var(--brand-blue); color: var(--white); border-radius: 17px;
    display: flex; align-items: center; justify-content: center; gap: 12px;
    font-size: 30px; font-weight: 400; text-decoration: none;
  }
  .download-button svg { width: 34px; height: 34px; }
  .book-cover {
    position: absolute; left: 451px; top: 41px; width: 169px; height: 255px;
    background: linear-gradient(160deg, #f4eef0 0%, #d8a6b8 45%, #c23a6e 100%);
  }

  /* Footer */
  .site-footer {
    height: 115px; background: var(--brand-blue);
    display: flex; align-items: center; justify-content: space-between;
    padding: 0 40px 0 64px;
  }
  .footer-links { display: flex; gap: 22px; }
  .footer-links a { color: var(--white); font-size: 28px; text-decoration: none; }
  .social-link {
    display: flex; align-items: center; gap: 12px;
    color: var(--white); font-size: 24px; text-decoration: none;
  }
  .social-link .square { width: 26px; height: 26px; background: var(--white); }
</style>
</head>
<body>
<div class="canvas">
  <main class="mobile-screen">

    <header class="site-header">
      <div class="menu-toggle" aria-label="Menu"><span></span><span></span><span></span></div>
      <div class="brand-name">Sabine Ter Horst</div>
    </header>

    <nav class="category-nav" aria-label="Categories">
      <svg class="category-icon" viewBox="0 0 90 90" aria-label="Eye makeup">
        <path d="M6 46 Q45 10 84 46" fill="none" stroke="#3b5998" stroke-width="5" stroke-linecap="round"/>
        <path d="M12 44 Q45 28 78 44 Q45 68 12 44 Z" fill="none" stroke="#3b5998" stroke-width="5" stroke-linejoin="round"/>
        <path d="M20 58 L14 66 M32 63 L28 72 M45 65 L45 74 M58 63 L62 72 M70 58 L76 66" stroke="#3b5998" stroke-width="4" stroke-linecap="round"/>
      </svg>
      <svg class="category-icon" viewBox="0 0 90 90" aria-label="Skin care">
        <path d="M45 84 C16 70 10 40 26 14 C46 22 56 54 45 84 Z" fill="#3b5998"/>
        <path d="M45 84 C66 70 82 46 80 20 C58 24 46 54 45 84 Z" fill="#3b5998"/>
        <path d="M45 84 C30 64 14 58 4 60 C12 76 30 84 45 84 Z" fill="#3b5998"/>
      </svg>
      <svg class="category-icon" viewBox="0 0 90 90" aria-label="E-book shop">
        <rect x="20" y="8" width="50" height="74" rx="7" fill="#3b5998"/>
        <rect x="27" y="16" width="36" height="52" fill="#fff"/>
        <path d="M31 23 H59 M31 30 H59 M31 37 H59 M31 44 H59 M31 51 H59 M31 58 H59" stroke="#3b5998" stroke-width="3"/>
      </svg>
      <svg class="category-icon" viewBox="0 0 90 90" aria-label="About Sabine">
        <circle cx="45" cy="45" r="34" fill="#3b5998"/>
      </svg>
    </nav>

    <section class="hero-banner">
      <h1 class="hero-title">LOVELY COLORS</h1>
      <div class="hero-photo" role="img" aria-label="Photo of a row of lipsticks in nude, red, berry and violet shades"></div>
    </section>

    <section class="guide-promo">
      <h2 class="guide-heading">How to apply<br>makeup<br>like the pros do</h2>
      <a class="download-button" href="#">
        <svg viewBox="0 0 34 34" aria-hidden="true">
          <path d="M17 3 V21 M9 13 L17 21 L25 13" fill="none" stroke="#fff" stroke-width="3.5" stroke-linecap="round" stroke-linejoin="round"/>
          <path d="M4 22 V30 H30 V22" fill="none" stroke="#fff" stroke-width="3.5" stroke-linejoin="round"/>
        </svg>
        Download
      </a>
      <div class="book-cover" role="img" aria-label="Cover of the Rosa Lindqvist Makeup Handbook with a makeup brush and pink powder"></div>
    </section>

    <footer class="site-footer">
      <div class="footer-links">
        <a href="#">Contact</a>
        <a href="#">About</a>
      </div>
      <a class="social-link" href="#"><span class="square"></span>Circlefeed</a>
    </footer>

  </main>
</div>
</body>
</html>
```